Design a Restaurant Menu for Modern Japanese Restaurant

Please design a Restaurant Menu for Modern Japanese Restaurant.
Following is the sample menu design.
No need to be similar with sample design, but prefer with this layout
(of cause you can change around the layout)
First page
https://www.quillvault.com/s/mr7pk2zqe55wbnj/top_menu_first_page.pdf?dl=0
Secand and Third page
https://www.quillvault.com/s/hgs3ruyw82cfq0t/Secand_and%20Third_page.doc?dl=0
Last page
https://www.quillvault.com/s/wzt6mlpa19xjkrb/Last_page.doc?dl=0
total 4 pages with A4 size. (like a 2 page book)
design taste: Simple, conspicuous, easy viewing.
you can use any photo from the following link and website.
photo link
https://www.quillvault.com/sh/k42mnbzrtqu8e/BBHTQrvLmPgWsaYuDeNhT47kd?dl=0
Website
http://tallowreedkitchen.com.au/4/TALLOW_REED_KITCHEN-TOP.html

```html
<!DOCTYPE html>
<html lang="en">
<head>
<meta charset="utf-8">
<title>Tallow Reed Kitchen — Menu</title>
<link rel="stylesheet" href="https://fonts.googleapis.com/css2?family=Josefin+Sans:wght@100;300;400&family=Roboto+Condensed:wght@400;700&display=swap">
<style>
  :root {
    --bg: #d9d9d9;
    --paper: #ffffff;
    --ink: #1a1a1a;
    --band: #0d0d0d;
    --silver: #cfcfcf;
    --wood-dark: #5a2f14;
    --wood-mid: #9a5a28;
    --wood-light: #c98a4c;
    --accent-red: #d3231e;
    --accent-orange: #e8731c;
    --blossom: #3a3a30;
    --blossom-light: #e9d36a;
  }
  * { box-sizing: border-box; margin: 0; padding: 0; }
  html, body { width: 1200px; height: 876px; overflow: hidden; }
  body {
    background: var(--bg);
    font-family: "Roboto Condensed", Arial, sans-serif;
    position: relative;
  }
  .page {
    position: absolute;
    top: 38px;
    width: 566px;
    height: 800px;
    overflow: hidden;
    box-shadow: 0 6px 18px rgba(0,0,0,.25);
  }
  .page--cover { left: 24px; background: var(--band); }
  .page--courses { left: 610px; background: var(--paper); }

  /* cover */
  .cover__band {
    position: absolute; left: 0; top: 0; width: 160px; height: 800px;
    background: linear-gradient(90deg, #050505, #1c1c1c);
  }
  .cover__band-corner {
    position: absolute; left: 12px; top: 14px; width: 26px; height: 26px;
    border-left: 2px solid #777; border-top: 2px solid #777;
  }
  .cover__title {
    position: absolute; left: 0; top: 100px; width: 160px;
    font-family: "Josefin Sans", sans-serif; font-weight: 100;
    font-size: 128px; line-height: 128px; text-align: center;
    color: var(--silver);
    background: linear-gradient(180deg, #f2f2f2, #8c8c8c 50%, #e6e6e6);
    -webkit-background-clip: text; background-clip: text;
    -webkit-text-fill-color: transparent;
  }
  .cover__title span { display: block; }
  .cover__wood {
    position: absolute; left: 160px; top: 0; width: 406px; height: 800px;
    background:
      radial-gradient(circle at 30% 6%, rgba(255,230,180,.55), transparent 18%),
      radial-gradient(circle at 70% 6%, rgba(255,230,180,.45), transparent 16%),
      repeating-linear-gradient(90deg, var(--wood-mid) 0 14px, var(--wood-dark) 14px 16px, var(--wood-light) 16px 30px, var(--wood-dark) 30px 32px);
  }
  .cover__blossom {
    position: absolute; left: 0; top: 560px; width: 200px; height: 240px;
    background: radial-gradient(ellipse at 60% 50%, var(--blossom) 0%, rgba(20,20,20,0) 70%);
  }
  .brand {
    position: absolute; left: 160px; width: 406px; top: 78px;
    display: flex; flex-direction: column; align-items: center; gap: 14px;
  }
  .brand__mark {
    width: 120px; height: 120px; border-radius: 50%;
    border: 3px solid #f1ece4;
  }
  .brand__name {
    font-family: "Josefin Sans", sans-serif; font-weight: 300;
    font-size: 22px; letter-spacing: 1px; color: #f4efe6;
  }
  .dish-photo {
    position: absolute; border-radius: 50%;
    border: 4px solid #f3f0ea;
  }
  .dish-photo--steak { left: 188px; top: 340px; width: 164px; height: 164px;
    background: radial-gradient(circle at 50% 45%, #6b3a22, #c4a23c 70%, #7d9a4a); }
  .dish-photo--wagyu { left: 394px; top: 250px; width: 160px; height: 160px;
    background: radial-gradient(circle at 50% 50%, #c8575a, #e8b0b0 55%, #6a8a45); }
  .dish-photo--coffee { left: 394px; top: 465px; width: 160px; height: 160px;
    background: radial-gradient(circle at 50% 50%, #6e4a36, #efe9e2 50%, #a79f96); }
  .dish-photo--sake { left: 230px; top: 560px; width: 150px; height: 150px;
    background: radial-gradient(circle at 50% 50%, #f2f2f2, #2f4a8c 70%, #b02020); }

  /* course pages */
  .courses__band {
    position: absolute; left: 0; top: 0; width: 566px; height: 88px;
    background: var(--band);
  }
  .courses__brand {
    position: absolute; right: 132px; top: 42px;
    font-family: "Josefin Sans", sans-serif; font-weight: 300;
    font-size: 24px; color: var(--accent-orange);
  }
  .courses__mark {
    position: absolute; right: 18px; top: 12px; width: 100px; height: 100px;
    border-radius: 50%; border: 3px solid #f1ece4; background: var(--band);
  }
  .courses__title {
    position: absolute; left: 214px; top: 102px;
    font-family: "Josefin Sans", sans-serif; font-weight: 400;
    font-size: 17px; letter-spacing: .5px; color: var(--ink);
  }
  .course {
    position: absolute; top: 102px;
    font-size: 7px; line-height: 9.2px; color: #333; text-transform: uppercase;
  }
  .course--five { left: 30px; width: 170px; }
  .course--four { left: 214px; top: 128px; width: 168px; }
  .course__head { color: var(--accent-red); font-weight: 700; font-size: 7.5px; }
  .course__dish { margin-top: 6px; }
  .course__dish b { display: block; font-weight: 700; color: var(--ink); }
  .course__or { margin-top: 6px; color: #666; }
  .course__and { margin-top: 8px; color: var(--accent-red); font-weight: 700; }
  .course__note { margin-top: 10px; color: #555; }
  .side-photo { position: absolute; }
  .side-photo--canape { left: 400px; top: 120px; width: 166px; height: 170px;
    background: linear-gradient(160deg, #f6f6f0, #9cc46a 50%, #e7c65a); }
  .side-photo--round { left: 362px; top: 240px; width: 150px; height: 150px; border-radius: 50%;
    border: 4px solid #fff; background: radial-gradient(circle, #c8575a, #e7b3b0 55%, #6a8a45); }
  .side-photo--blossom { left: 430px; top: 400px; width: 136px; height: 290px;
    background: radial-gradient(ellipse at 60% 50%, rgba(233,211,106,.5), rgba(255,255,255,0) 70%); }
  .side-photo--plate { left: 330px; top: 640px; width: 236px; height: 160px;
    background: linear-gradient(160deg, #ffffff 10%, #7a4a30 45%, #e3a32c 80%); }
</style>
</head>
<body>

<section class="page page--cover">
  <div class="cover__wood" role="img" aria-label="Warm lit wooden wall panelling"></div>
  <div class="cover__band"><div class="cover__band-corner"></div></div>
  <h1 class="cover__title"><span>M</span><span>E</span><span>N</span><span>U</span></h1>
  <div class="cover__blossom" role="img" aria-label="Flowering plum branch"></div>
  <div class="brand">
    <div class="brand__mark"></div>
    <div class="brand__name">Tallow Reed Kitchen</div>
  </div>
  <div class="dish-photo dish-photo--steak" role="img" aria-label="Seared beef on golden rice"></div>
  <div class="dish-photo dish-photo--wagyu" role="img" aria-label="Wagyu cubes with greens"></div>
  <div class="dish-photo dish-photo--coffee" role="img" aria-label="Cups of dessert and coffee"></div>
  <div class="dish-photo dish-photo--sake" role="img" aria-label="Sake barrel"></div>
</section>

<section class="page page--courses">
  <div class="courses__band"></div>
  <div class="courses__brand">Tallow Reed Kitchen</div>
  <div class="courses__mark"></div>
  <h2 class="courses__title">SETCOURSEMENU</h2>

  <div class="course course--five">
    <div class="course__head">Tokutoku (5 course) $95 / person<br>(1 entree / 1 main / 1 dessert)</div>
    <div class="course__dish"><b>Sashimi (cold)</b>Fresh sashimi combination<br>(all salmon or tuna option ex $3)</div>
    <div class="course__or">or</div>
    <div class="course__dish"><b>Osuimono (soup)</b>Unagi eel, soft tofu, mushrooms, wakame<br>dashi broth</div>
    <div class="course__or">or</div>
    <div class="course__dish"><b>Caviar pasta</b>Angel hair pasta, tobiko caviar, mushrooms<br>creamy rice wine sauce<br>(additional soft shell crab ex $5)</div>
    <div class="course__or">or</div>
    <div class="course__dish"><b>Salmon &amp; scallop</b>Roasted salmon, scallop, tobiko caviar<br>yuzu mascarpone, orange miso</div>
    <div class="course__or">or</div>
    <div class="course__dish"><b>Pork &amp; pork</b>Pork belly, fillets, bacon, apple mango chilli sauce</div>
    <div class="course__and">and</div>
    <div class="course__dish"><b>Oceans</b>Barramundi, garfish, prawn, sweet potato<br>fresh greens, thai chilli plum miso</div>
    <div class="course__or">or</div>
    <div class="course__dish"><b>Tenderloin steak</b>Beef tenderloin fillet, mushrooms, potato<br>greens and creamy red wine sauce</div>
    <div class="course__or">or</div>
    <div class="course__dish"><b>Duck leg confit</b>Duck leg, scallops, tempura onion<br>mash potato, pumpkin puree, duck jus</div>
    <div class="course__or">or</div>
    <div class="course__dish"><b>Lamb duo</b>Grilled lamb steak, braised shoulder<br>mash potato, balsamic soy dressing</div>
    <div class="course__and">and</div>
    <div class="course__dish"><b>Blood orange &amp; coconut gelato</b>Crushed mixed nuts</div>
    <div class="course__or">or</div>
    <div class="course__dish"><b>Matcha brulee</b>Green tea custard</div>
    <div class="course__note">Dishes may vary with available produce<br>prices and seasonal availability subject to change</div>
  </div>

  <div class="course course--four">
    <div class="course__head">Osusume (4 course) $80 / person<br>(2 entrees / 1 main / 1 dessert)</div>
    <div class="course__dish"><b>Sashimi (cold)</b>Fresh sashimi combination<br>(all salmon or tuna option ex $3)</div>
    <div class="course__or">or</div>
    <div class="course__dish"><b>Beef tataki (cold)</b>Grilled beef tenderloin fillet, yakumi<br>ponzu, yuzu dressing</div>
    <div class="course__or">or</div>
    <div class="course__dish"><b>Osuimono (soup)</b>Unagi eel, soft tofu, mushrooms, wakame<br>dashi broth</div>
    <div class="course__and">and</div>
    <div class="course__dish"><b>Caviar pasta</b>Angel hair pasta, tobiko caviar, mushrooms<br>(additional soft shell crab ex $5)</div>
    <div class="course__or">or</div>
    <div class="course__dish"><b>Salmon &amp; scallop</b>Roasted salmon, scallop, tobiko caviar<br>yuzu mascarpone, orange miso</div>
    <div class="course__or">or</div>
    <div class="course__dish"><b>Pork &amp; pork</b>Pork belly, fillets, bacon, apple mango chilli sauce</div>
    <div class="course__and">and</div>
    <div class="course__dish"><b>Oceans</b>Barramundi, garfish, prawn, sweet potato<br>fresh greens, thai chilli plum miso</div>
    <div class="course__or">or</div>
    <div class="course__dish"><b>Tenderloin steak</b>Beef tenderloin fillet, mushrooms, potato<br>greens and creamy red wine sauce</div>
    <div class="course__or">or</div>
    <div class="course__dish"><b>Lamb duo</b>Grilled lamb steak, braised shoulder<br>mash potato, balsamic soy dressing</div>
    <div class="course__and">and</div>
    <div class="course__dish"><b>Blood orange &amp; coconut gelato</b>Crushed mixed nuts</div>
    <div class="course__or">or</div>
    <div class="course__dish"><b>Espresso panna cotta</b>Coffee jelly</div>
  </div>

  <div class="side-photo side-photo--canape" role="img" aria-label="Canapés on skewers"></div>
  <div class="side-photo side-photo--round" role="img" aria-label="Wagyu cubes with greens"></div>
  <div class="side-photo side-photo--blossom" role="img" aria-label="Flowering plum branch"></div>
  <div class="side-photo side-photo--plate" role="img" aria-label="Seared beef on golden rice"></div>
</section>

</body>
</html>
```